Business card design for Automotive workshop

We need a business card for a new automotive repair and tyre shop called Gearwell Prime Automotive located in New Zealand. We are a clean, modern and fresh workshop and company.

Front needs to feature logo,
my name:
Corwin Pettigrew (director)

Address:
48 Larch Drive
Whitianga 3510

Phone: 07 842 3917
Mobile: 027 519 2746
Email: office@gearwellautomotive.co.nz
Website: gearwellautomotive.co.nz

Back needs to feature an area to write down appointment details, date and time.

Also feature a list of jobs and work we do such as,
Vehicle Servicing
All Mechanical Repairs
Warrant of Fitness
Tyres & Wheel Alignments
Automotive Diagnostics
Automotive Parts & Supplies

```html
<!DOCTYPE html>
<html lang="en">
<head>
<meta charset="utf-8">
<title>Gearwell Prime Automotive – Business Card</title>
<link rel="stylesheet" href="https://fonts.googleapis.com/css2?family=Montserrat:wght@400;500;700&family=Oswald:wght@600&display=swap">
<style>
  :root {
    --page: #0d0d0e;
    --card: #1e1e1f;
    --ink-emboss: #3c3c3e;
    --ink-soft: #55555a;
    --ink-logo: #8a8a8f;
    --ink-white: #f2f2f2;
    --accent-red: #e0202a;
  }
  * { box-sizing: border-box; margin: 0; padding: 0; }
  html, body { width: 1200px; height: 900px; overflow: hidden; }
  body {
    background: var(--page);
    font-family: "Montserrat", sans-serif;
    display: flex;
    flex-direction: column;
    align-items: center;
    justify-content: center;
    gap: 44px;
  }
  .card {
    width: 620px;
    height: 378px;
    background: var(--card);
    position: relative;
  }
  /* Services side */
  .card--services {
    display: flex;
    flex-direction: column;
    align-items: center;
    justify-content: center;
    gap: 44px;
  }
  .brand {
    display: flex;
    align-items: center;
    gap: 14px;
  }
  .brand__mark {
    width: 14px; height: 14px;
    background: var(--ink-logo);
  }
  .brand__name {
    font-weight: 700;
    font-size: 30px;
    letter-spacing: 1px;
    text-transform: uppercase;
    color: var(--ink-logo);
  }
  .services {
    list-style: none;
    display: flex;
    flex-wrap: wrap;
    justify-content: center;
    gap: 4px 14px;
    width: 560px;
    color: var(--ink-white);
    font-size: 15px;
    font-weight: 500;
    letter-spacing: 0.3px;
  }
  .services li { display: flex; align-items: center; gap: 5px; }
  .services li::before {
    content: "";
    width: 6px; height: 6px;
    border-radius: 50%;
    background: var(--accent-red);
  }
  /* Contact side */
  .contact-block {
    position: absolute;
    left: 24px; right: 24px; top: 104px;
    display: flex;
    align-items: flex-start;
    gap: 18px;
  }
  .person {
    flex: 0 0 262px;
    text-align: right;
    padding-top: 10px;
  }
  .person__name {
    font-family: "Oswald", sans-serif;
    font-weight: 600;
    font-size: 30px;
    letter-spacing: 0.3px;
    text-transform: uppercase;
    color: var(--ink-emboss);
    line-height: 1.1;
    white-space: nowrap;
  }
  .person__role {
    font-size: 15px;
    color: var(--ink-soft);
    margin-top: 4px;
  }
  .divider {
    flex: none;
    width: 1px; height: 100px;
    background: var(--ink-soft);
  }
  .contacts {
    list-style: none;
    display: flex;
    flex-direction: column;
    gap: 4px;
    padding-top: 4px;
    color: var(--ink-soft);
    font-size: 15px;
    white-space: nowrap;
  }
  .contacts li { display: flex; align-items: center; gap: 10px; }
  .icon { width: 14px; height: 14px; flex: none; }
  .address {
    position: absolute;
    left: 150px; bottom: 56px;
    display: flex; align-items: center; gap: 8px;
    color: var(--ink-soft);
    font-size: 17px;
  }
</style>
</head>
<body>
  <section class="card card--services">
    <div class="brand">
      <span class="brand__mark"></span>
      <span class="brand__name">Gearwell Prime Automotive</span>
    </div>
    <ul class="services">
      <li>Vehicle Servicing</li>
      <li>All Mechanical Repairs</li>
      <li>Warrant of Fitness</li>
      <li>Tyres &amp; Wheel Alignments</li>
      <li>Automotive Diagnostics</li>
      <li>Automotive Parts &amp; Supplies</li>
    </ul>
  </section>

  <section class="card card--contact">
    <div class="contact-block">
      <div class="person">
        <p class="person__name">Corwin Pettigrew</p>
        <p class="person__role">Director</p>
      </div>
      <div class="divider"></div>
      <ul class="contacts">
        <li>
          <svg class="icon" viewBox="0 0 16 16"><path d="M4 1.5 6 4.5 4.8 6c.8 2 2.5 3.7 4.5 4.5L10.8 9.3l3 2-1.2 2.5C7 13.3 2.7 9 2 3.5z" fill="none" stroke="currentColor" stroke-width="1.3"/></svg>
          07 842 3917
        </li>
        <li>
          <svg class="icon" viewBox="0 0 16 16"><rect x="4" y="1.5" width="8" height="13" rx="1.5" fill="none" stroke="currentColor" stroke-width="1.3"/><line x1="7" y1="12" x2="9" y2="12" stroke="currentColor" stroke-width="1.3"/></svg>
          027 519 2746
        </li>
        <li>
          <svg class="icon" viewBox="0 0 16 16"><rect x="1.5" y="3.5" width="13" height="9" fill="none" stroke="currentColor" stroke-width="1.3"/><path d="M1.5 3.5 8 9l6.5-5.5" fill="none" stroke="currentColor" stroke-width="1.3"/></svg>
          office@gearwellautomotive.co.nz
        </li>
        <li>
          <svg class="icon" viewBox="0 0 16 16"><circle cx="8" cy="8" r="6.5" fill="none" stroke="currentColor" stroke-width="1.3"/><ellipse cx="8" cy="8" rx="3" ry="6.5" fill="none" stroke="currentColor" stroke-width="1.1"/><line x1="1.5" y1="8" x2="14.5" y2="8" stroke="currentColor" stroke-width="1.1"/></svg>
          gearwellautomotive.co.nz
        </li>
      </ul>
    </div>
    <p class="address">
      <svg class="icon" viewBox="0 0 16 16"><path d="M8 15S3 9.5 3 6a5 5 0 0 1 10 0c0 3.5-5 9-5 9z" fill="none" stroke="currentColor" stroke-width="1.3"/><circle cx="8" cy="6" r="1.8" fill="none" stroke="currentColor" stroke-width="1.2"/></svg>
      48 Larch Drive Whitianga 3510
    </p>
  </section>
</body>
</html>
```